Monthly/Holiday Graphics for Retail Store Starting w/ Valentines Day

We need a retail ads designed for our jewelry store, Velvet Lark, for each month and major holidays. We will start with a Valentines Day ad. <br/><br/>The idea behind the promotion is for women to come in and pick out a few items and put on their "shopping list" that we will keep for them in the store. We will then email the husbands letting them know that we have a few options already pre-approved by their wife. All they have to do is come pick from the shopping list and she will definitely get something that she wants. <br/><br/>The tagline will be "Get exactly what you asked for at Velvet Lark"<br/><br/>Brand Colors<br/> Dark Purple - RGB: 100 33 101 CMYK: 68 100 29 17 Hex: #642165<br/> Light Purple - RGB: 159 98 157 CMYK: 44 71 8 0 Hex: #9A629D<br/> Grey - RGB: 152 156 158 CMYK: 43 33 33 1 Hex: #989C9E<br/><br/><br/>Brand Fonts<br/> Berkshire Swash<br/> Lato<br/><br/>The website where you can pull product photos (heart jewelry should be included): www.velvetlarkshop.example<br/><br/>I have attached pictures below. No need to use all of the images in one graphic. I simply wanted to provide design element options. <br/><br/>I have also included a screencap of an ad that I liked. Doesn't have to be based upon this, I just like the clean and simple design. Also note that this company is offering a discount and we are not. <br/><br/>Thank you!

```html
<!DOCTYPE html>
<html lang="en">
<head>
<meta charset="utf-8">
<title>Velvet Lark – Valentines Day Shopping List</title>
<link rel="stylesheet" href="https://fonts.googleapis.com/css2?family=Lato:wght@400&display=swap">
<style>
  :root {
    --dark-purple: #642165;
    --light-purple: #9a629d;
    --brand-purple: #8b3a8e;
    --white: #ffffff;
    --page: #ffffff;
  }
  html, body {
    margin: 0;
    padding: 0;
    width: 1200px;
    height: 1200px;
    overflow: hidden;
    background: var(--page);
  }
  .ad {
    display: block;
    width: 1200px;
    height: 1200px;
  }
  .ad__field { fill: var(--dark-purple); }
  .ad__heart { fill: var(--light-purple); }
  .ad__envelope-band { fill: var(--light-purple); }
  .ad__envelope-flap { fill: var(--white); }
  .tagline {
    font-family: "Lato", sans-serif;
    font-weight: 400;
    font-size: 34px;
    fill: var(--white);
  }
  .tagline__name {
    font-family: "Lato", sans-serif;
    font-weight: 400;
    font-size: 66px;
    fill: var(--light-purple);
  }
  .heart-copy {
    font-family: "Lato", sans-serif;
    font-weight: 400;
    fill: var(--white);
  }
  .heart-copy--small { font-size: 15.5px; }
  .heart-copy--large { font-size: 19px; }
  .brand-name {
    font-family: "Lato", sans-serif;
    font-weight: 400;
    font-size: 80px;
    fill: var(--brand-purple);
  }
  .product-photo--ring { fill: url(#ringTone); }
  .product-photo--pendant { fill: url(#pendantTone); }
</style>
</head>
<body>
<svg class="ad" viewBox="0 0 900 900" xmlns="http://www.w3.org/2000/svg" aria-labelledby="adTitle">
  <title id="adTitle">Velvet Lark Valentines Day advertisement</title>
  <defs>
    <filter id="cardShadow" x="-5%" y="-5%" width="110%" height="110%">
      <feDropShadow dx="2" dy="3" stdDeviation="3" flood-color="#000" flood-opacity="0.25"/>
    </filter>
    <linearGradient id="ringTone" x1="0" y1="0" x2="1" y2="1">
      <stop offset="0" stop-color="#e4e8ea"/>
      <stop offset="1" stop-color="#a9bcc4"/>
    </linearGradient>
    <radialGradient id="pendantTone" cx="0.5" cy="0.65" r="0.6">
      <stop offset="0" stop-color="#7a3f9a"/>
      <stop offset="1" stop-color="#3d1456"/>
    </radialGradient>
    <clipPath id="cardClip">
      <rect x="88" y="82" width="720" height="736"/>
    </clipPath>
  </defs>

  <g class="ad__card" filter="url(#cardShadow)">
    <rect class="ad__field" x="88" y="82" width="720" height="736"/>
  </g>

  <g clip-path="url(#cardClip)">
    <path class="ad__heart" d="M450 470 C400 420 325 378 325 308 C325 268 355 246 390 246 C420 246 440 263 450 282 C460 263 480 246 510 246 C545 246 575 268 575 308 C575 378 500 420 450 470 Z"/>
    <polygon class="ad__envelope-band" points="88,778 450,448 808,778 808,818 88,818"/>
    <polygon class="ad__envelope-flap" points="112,818 440,518 450,492 460,518 788,818"/>
  </g>

  <text class="tagline" x="450" y="152" text-anchor="middle">Get exactly what you asked for at</text>
  <text class="tagline__name" x="450" y="220" text-anchor="middle">Velvet Lark</text>

  <rect class="product-photo--ring" x="370" y="238" width="140" height="70" rx="18"
        role="img" aria-label="Product photo: silver ring with an emerald-cut pale blue gemstone"/>

  <text class="heart-copy heart-copy--small" x="450" y="346" text-anchor="middle">PICK YOUR PERFECT GIFT</text>
  <text class="heart-copy heart-copy--large" x="450" y="374" text-anchor="middle">ON</text>
  <text class="heart-copy heart-copy--large" x="450" y="400" text-anchor="middle">VALENTINES DAY</text>

  <rect class="product-photo--pendant" x="418" y="528" width="66" height="122" rx="30"
        role="img" aria-label="Product photo: silver box chain necklace with a wire-wrapped purple amethyst teardrop pendant"/>

  <text class="brand-name" x="450" y="768" text-anchor="middle">Velvet Lark</text>
</svg>
</body>
</html>
```